Kestrel Roofing & Restoration Business Card Design

Lookiing for a double sided business card design that will have rounded corners, will look good with Spot UV, Soft Laminate, or Gloss
Front of card should have Logo, Name and Contact Info, License numbers
Back of card should have Logo, maybe other small details

```html
<!DOCTYPE html>
<html lang="en">
<head>
<meta charset="utf-8">
<title>Kestrel Roofing &amp; Restoration — Business Card</title>
<link href="https://fonts.googleapis.com/css2?family=Poppins:wght@500;600&family=Nunito+Sans:wght@400;600&display=swap" rel="stylesheet">
<style>
  :root {
    --backdrop: #141414;
    --card: #1f1f20;
    --card-edge: #262627;
    --ink: #f2f2f2;
    --ink-soft: #d9d9d9;
    --accent: #29a8e0;
    --emboss: #1a1a1b;
  }
  * { margin: 0; padding: 0; box-sizing: border-box; }
  html, body { width: 1200px; height: 1059px; overflow: hidden; background: var(--backdrop); }
  body { position: relative; font-family: "Nunito Sans", Arial, sans-serif; color: var(--ink); }

  .card {
    position: absolute;
    border-radius: 20px;
    overflow: hidden;
    box-shadow: 0 10px 24px rgba(0,0,0,0.55);
  }
  .card--front { left: 257px; top: 89px; width: 687px; height: 390px; background: var(--card); }
  .card--back  { left: 253px; top: 546px; width: 694px; height: 394px; }

  .wordmark {
    position: absolute; left: 38px; top: 50px;
    font-family: "Poppins", Arial, sans-serif; font-weight: 600;
    font-size: 22px; line-height: 29px; letter-spacing: 0.3px;
    color: var(--ink); text-transform: uppercase;
  }

  .holder { position: absolute; right: 31px; top: 55px; text-align: right; }
  .holder__name {
    font-family: "Poppins", Arial, sans-serif; font-weight: 600;
    font-size: 23px; line-height: 26px; color: var(--accent); letter-spacing: 0.2px;
  }
  .holder__title { font-size: 15px; line-height: 20px; color: var(--ink-soft); margin-top: 2px; letter-spacing: 0.3px; }
  .holder__bar { position: absolute; right: 0; top: 59px; width: 15px; height: 36px; background: var(--accent); }

  .contact { position: absolute; left: 38px; top: 196px; font-size: 16px; line-height: 20px; color: var(--ink-soft); }
  .contact__address p { margin: 0; }
  .contact__license { margin-top: 9px; }
  .contact__license span { color: var(--accent); }
  .contact__list { list-style: none; margin-top: 11px; }
  .contact__list li { display: flex; align-items: center; gap: 7px; height: 27px; }
  .contact__list svg { width: 13px; height: 13px; fill: var(--accent); flex: none; }

  .emboss {
    position: absolute; right: 22px; top: 220px;
    font-family: "Poppins", Arial, sans-serif; font-weight: 600;
    font-size: 78px; line-height: 1; color: var(--emboss); letter-spacing: 1px;
    text-shadow: 0 1px 0 #2a2a2b;
  }

  .card__field {
    position: absolute; inset: 0;
    background: linear-gradient(90deg, #161617 0%, #1c1c1d 40%, #3a3a3b 75%, #8a8a8b 100%);
  }
  .card__mark {
    position: absolute; right: 131px; top: 308px;
    font-family: "Poppins", Arial, sans-serif; font-weight: 600;
    font-size: 28px; line-height: 36px; color: #ffffff; letter-spacing: 0.5px;
  }
</style>
</head>
<body>
  <section class="card card--front" aria-label="Card front">
    <div class="wordmark">Kestrel Roofing &amp;<br>Restoration</div>

    <div class="holder">
      <div class="holder__name">MARCUS HALE</div>
      <div class="holder__title">Founder &amp; CEO</div>
    </div>
    <div class="holder__bar"></div>

    <div class="contact">
      <div class="contact__address">
        <p>480 Ridge Line Road</p>
        <p>Fairview, Ohio 45402</p>
      </div>
      <div class="contact__license"><span>License No:</span> 123456</div>
      <ul class="contact__list">
        <li>
          <svg viewBox="0 0 24 24" aria-hidden="true"><path d="M6.6 10.8a15.1 15.1 0 0 0 6.6 6.6l2.2-2.2a1 1 0 0 1 1-.25 11.4 11.4 0 0 0 3.6.57 1 1 0 0 1 1 1V20a1 1 0 0 1-1 1A17 17 0 0 1 3 4a1 1 0 0 1 1-1h3.5a1 1 0 0 1 1 1c0 1.25.2 2.45.57 3.57a1 1 0 0 1-.25 1z"/></svg>
          (555) 014-2290
        </li>
        <li>
          <svg viewBox="0 0 24 24" aria-hidden="true"><path d="M2 5h20v14H2z M2 5l10 8 10-8" fill="var(--accent)"/><path d="M3 6l9 7 9-7" fill="none" stroke="var(--card)" stroke-width="1.6"/></svg>
          info@kestrelroofing.com
        </li>
        <li>
          <svg viewBox="0 0 24 24" aria-hidden="true"><circle cx="12" cy="12" r="10"/><path d="M2 12h20M12 2c3 3 3 17 0 20M12 2c-3 3-3 17 0 20" fill="none" stroke="var(--card)" stroke-width="1.5"/></svg>
          www.kestrelroofing.com
        </li>
      </ul>
    </div>

    <div class="emboss" aria-hidden="true">KESTREL</div>
  </section>

  <section class="card card--back" aria-label="Card back">
    <div class="card__field" role="img" aria-label="Repeating brand pattern fading from black to grey, spot UV finish"></div>
    <div class="card__mark">KESTREL</div>
  </section>
</body>
</html>
```